Automotive Locksmiith company needs a website design and mobile website

We need a website design and a mobile design for an automotive locksmith company called Cedarline Autoworks LLC.We are based in the center of the Dallas-Fort Worth Metroplex. We have a website that was directed more towards the towing services we also offer. We would like to have it more towards our locksmith products. Our main services include:
Auto keys duplication
Cutting of new car keys
Car Lockouts
Laser key replacement
Cutting keys by code
Broken key extractions
Production of transponder keys
Key fob programming
Door lock repairs
Ignition repairs/replacement
We work on 95% of the automotive market that includes Vorra, Belvo, KTZ, Merrowind, Tanquelle, Polgrave, Brunt, QR, Solvane, Pirel, Zoravelo, Uto, Harwick, Quorel, Telvar, Ostravin, Fendale, Pavo, Rulko Kelvarona , Brisel, Varuno, Drexmotor, Tesko.
We are one of the most affordable services in the DFW area . Our prices for transponder copies start at $35 per key. We provide services for high-end vehicles also as KTZ and Ostravin. We can program the new proximity keys for Telvar Vehicles 2013-up. We also work on the new Pell Vehicles 20-13 and up including the Pell Caravel head remote key.
We would like to have a similar style to the website we already have with the option to schedule an appointment on the mobile website. This mobile application will deliver an email when a new customer is requiring the service. It will ask for Year, Make, Model , Service to be performed( Key copy, Lockout, Lost Key, Change Ignition lock, change door lock, Other services.) Description of the service to be performed, Address, Select time of service.
Our current website is cedarlineautoworks.example

Reason: Need pictures of webpages inside design (about us , location etc) and mobile pictures( how website looks in zelPad / norvix)

Automotive

• check word attachment

```html
<!DOCTYPE html>
<html lang="en">
<head>
<meta charset="utf-8">
<title>Cedarline Autoworks LLC</title>
<link href="https://fonts.googleapis.com/css2?family=Open+Sans:ital,wght@0,400;0,600;0,700;1,400&family=Raleway:wght@300;400;600&display=swap" rel="stylesheet">
<style>
:root{
  --teal:#22a7c8;
  --navy:#14304f;
  --ink:#1c2530;
  --dark:#1f2b35;
  --text:#333a40;
  --muted:#6b7177;
  --panel:#f2f2f0;
  --band:#d9dbd5;
  --strip:#ececea;
  --red:#ee4f43;
  --rule:#e2e4e6;
  --white:#ffffff;
}
*{box-sizing:border-box;margin:0;padding:0}
html,body{width:1200px;height:2699px;overflow:hidden;background:var(--white)}
body{position:relative;font-family:'Open Sans',sans-serif;color:var(--text)}
.abs{position:absolute}
.brand-name{font-family:'Open Sans',sans-serif;font-weight:700;color:var(--navy);letter-spacing:-.3px}
/* header */
.site-header{left:0;top:0;width:1200px;height:138px}
.logo{left:36px;top:58px;display:flex;align-items:center;gap:10px;font-size:21px}
.logo .mark{width:18px;height:18px;background:var(--teal)}
.phone-pill{left:1031px;top:48px;width:140px;height:28px;border-radius:14px;background:var(--dark);color:#fff;font-size:13px;display:flex;align-items:center;justify-content:center;gap:8px}
.main-nav{left:509px;top:97px;display:flex;font-size:12px;font-weight:600;color:var(--ink);text-transform:uppercase}
.main-nav a{color:inherit;text-decoration:none;height:29px;line-height:29px}
.main-nav .active{background:var(--teal);color:#fff;padding:0 17px;margin-right:24px}
.main-nav .n2{margin-right:35px}.main-nav .n3{margin-right:32px}.main-nav .n4{margin-right:33px}.main-nav .n5{margin-right:33px}
/* hero */
.hero{left:0;top:138px;width:1200px;height:382px;background:linear-gradient(100deg,#6f6a64 0%,#9a948c 40%,#c9c4bc 70%,#8d8a86 100%)}
.hero-title{left:0;top:222px;width:1200px;text-align:center;font-family:'Raleway',sans-serif;font-weight:300;font-size:31px;line-height:34px;color:#fff}
.hero-sub{left:300px;top:447px;width:600px;text-align:center;font-size:15.5px;line-height:27px;color:#fff}
.hero-arrow{top:320px;width:34px;height:36px;background:rgba(20,25,30,.8);display:flex;align-items:center;justify-content:center}
/* call band */
.cta-band{left:0;top:520px;width:1200px;height:162px}
.cta-icon{top:0;width:139px;height:162px;background:var(--dark);display:flex;align-items:center;justify-content:center}
.cta-panel{top:0;height:162px;background:var(--band);font-family:'Raleway',sans-serif;font-weight:300;font-size:47px;line-height:42px;color:var(--ink);padding-left:46px;padding-top:38px}
/* brands */
.brands{left:0;top:682px;width:1200px;height:131px;background:var(--strip)}
.brands h2{position:absolute;top:18px;width:1200px;text-align:center;font-family:'Raleway',sans-serif;font-weight:300;font-size:27px;color:var(--ink)}
.brand-row{position:absolute;left:52px;top:70px;width:1096px;display:flex;justify-content:space-between;align-items:center;font-size:12px;font-weight:700;color:#222;letter-spacing:.3px}
.brand-arrow{top:740px;width:30px;height:48px;background:#c9cbc7;display:flex;align-items:center;justify-content:center}
/* section headings */
.section-title{left:63px;width:1081px;font-family:'Raleway',sans-serif;font-weight:400;font-size:24px;color:var(--ink);border-bottom:1px solid var(--rule);padding-bottom:10px}
/* about */
.about{left:63px;top:934px;width:1081px;height:223px;background:var(--panel)}
.about-photo{left:0;top:0;width:300px;height:223px;background:linear-gradient(135deg,#8b8f93,#dcdedf 55%,#a7abae)}
.about-text{left:337px;top:30px;width:705px;font-size:11.2px;line-height:15.5px;color:#444}
.about-text p{margin-bottom:12px}
/* services */
.service-card{top:1270px;width:528px;height:268px;background:var(--panel)}
.service-card.recovery{left:63px;border-bottom:2px solid var(--teal)}
.service-card.locksmith{left:617px;border-bottom:2px solid var(--navy)}
.tab{height:31px;line-height:31px;color:#fff;font-family:'Raleway',sans-serif;font-size:17px;padding-left:20px}
.service-list{position:absolute;left:26px;top:68px;list-style:none;font-size:12.5px;color:#222}
.service-list li{display:flex;align-items:center;gap:20px;height:30px}
/* coverage */
.coverage{left:63px;top:1569px;width:1081px;height:194px;background:var(--panel);border-bottom:2px solid var(--navy)}
.coverage-photo{left:0;top:0;width:326px;height:194px;background:linear-gradient(180deg,#6fa3cf 0%,#a9c7e0 45%,#5c6670 100%)}
.coverage-text{left:369px;top:35px;font-family:'Raleway',sans-serif;font-weight:300;font-size:22px;line-height:27px;color:var(--ink)}
.coverage-phone{left:362px;top:1671px;display:flex;align-items:center;gap:16px;font-family:'Raleway',sans-serif;font-weight:300;font-size:37px;color:var(--ink)}
.circle-icon{width:56px;height:56px;border-radius:50%;display:flex;align-items:center;justify-content:center}
/* facility */
.facility{left:63px;top:1795px;width:1081px;height:267px;background:var(--panel);border-bottom:2px solid var(--red)}
.facility-map{left:502px;top:0;width:579px;height:265px;background:linear-gradient(160deg,#d6dccb,#e7e9df 50%,#cfd6c4)}
.facility-text{left:113px;top:100px;font-family:'Raleway',sans-serif;font-weight:300;font-size:16.5px;line-height:24px;color:var(--ink)}
.facility-hours{font-size:31px;line-height:40px;margin-top:14px;display:block}
/* testimonials */
.testimonial-arrow{top:2221px;width:30px;height:40px;background:#e8e9e7;display:flex;align-items:center;justify-content:center}
.client-photo{left:186px;top:2181px;width:136px;height:136px;border-radius:50%;background:radial-gradient(circle at 50% 45%,#9b8a78,#3d352e 75%)}
.quote{left:394px;top:2205px;width:580px;font-style:italic;font-size:13.5px;line-height:22px;color:#333}
.quote b{font-weight:700}
/* footer */
.site-footer{left:0;top:2371px;width:1200px;height:328px;background:var(--panel);border-top:2px solid #bfe3ee}
.footer-card{left:63px;top:2362px;width:275px;height:306px;background:#fff;box-shadow:0 0 2px rgba(0,0,0,.15)}
.footer-card .brand-name{position:absolute;left:0;top:54px;width:275px;text-align:center;font-size:19px}
.footer-map{left:0;top:120px;width:275px;height:186px;background:linear-gradient(160deg,#dfe3d6,#eceee6 55%,#d4d9ca)}
.footer-info{left:374px;top:2398px;font-size:12.5px;line-height:22px;color:#222}
.footer-info h3{font-size:16.5px;font-weight:700;margin-bottom:2px}
.footer-info .mail{color:#2a70b8}
.social{left:374px;top:2556px;display:flex;gap:8px}
.social span{width:27px;height:27px;border-radius:50%;background:#2a2f35}
.footer-nav{left:745px;top:2398px;list-style:none;font-size:11.5px;font-weight:700;line-height:21.5px;color:#222;text-transform:uppercase}
.footer-arrow{left:712px;top:2403px}
.apps-title{left:970px;top:2400px;font-size:13px;color:#222}
.app-badge{left:973px;width:133px;height:41px;border-radius:6px;background:#111}
.copyright{left:374px;top:2631px;font-size:10.5px;color:#777;letter-spacing:.3px}
</style>
</head>
<body>

<header class="site-header abs">
  <div class="logo abs"><span class="mark"></span><span class="brand-name">Cedarline Autoworks</span></div>
  <div class="phone-pill abs">
    <svg width="14" height="14" viewBox="0 0 24 24" fill="none" stroke="#fff" stroke-width="2"><path d="M6 3h4l2 5-2.5 1.5a11 11 0 0 0 5 5L16 12l5 2v4a2 2 0 0 1-2 2A16 16 0 0 1 4 5a2 2 0 0 1 2-2z"/></svg>
    888-555-0142
  </div>
  <nav class="main-nav abs">
    <a class="active">Home</a><a class="n2">About Us</a><a class="n3">Services</a><a class="n4">Locksmith Services</a><a class="n5">Price List</a><a>Contact Us</a>
  </nav>
</header>

<section class="hero abs" role="img" aria-label="Smiling driver holding up a car key inside a vehicle"></section>
<h1 class="hero-title abs">Professional Automotive Locksmith Service<br>Special Price for Used Car Dealership!</h1>
<p class="hero-sub abs">Any model and year of the following makes: Brunt, Polgrave, Tanquelle, Galvern, Pell, Telvar, Zoravelo, Pirel, Rulko, Kelvarona, Varuno.</p>
<div class="hero-arrow abs" style="left:23px"><svg width="12" height="18" viewBox="0 0 12 18"><path d="M9 2 2 9l7 7" fill="none" stroke="#fff" stroke-width="2"/></svg></div>
<div class="hero-arrow abs" style="left:1143px"><svg width="12" height="18" viewBox="0 0 12 18"><path d="m3 2 7 7-7 7" fill="none" stroke="#fff" stroke-width="2"/></svg></div>

<section class="cta-band abs">
  <div class="cta-icon abs" style="left:0">
    <svg width="60" height="60" viewBox="0 0 24 24" fill="none" stroke="var(--teal)" stroke-width="1"><path d="M6 3h4l2 5-2.5 1.5a11 11 0 0 0 5 5L16 12l5 2v4a2 2 0 0 1-2 2A16 16 0 0 1 4 5a2 2 0 0 1 2-2z"/></svg>
  </div>
  <div class="cta-panel abs" style="left:139px;width:457px">Call us<br>888-555-0142</div>
  <div class="cta-icon abs" style="left:596px">
    <svg width="64" height="64" viewBox="0 0 64 64" fill="none" stroke="var(--teal)" stroke-width="1.6"><circle cx="32" cy="32" r="29"/><circle cx="32" cy="32" r="21"/><path d="M32 19v14h9"/></svg>
  </div>
  <div class="cta-panel abs" style="left:736px;width:464px">Schedule an<br>Appointment</div>
</section>

<section class="brands abs">
  <h2>We work on 95% of the automotive market that includes</h2>
  <div class="brand-row">
    <span>PIREL</span><span>OSTRAVIN</span><span>VORRA</span><span>RULKO</span><span>KTZ</span><span>PELL</span><span>KELVARONA</span><span>TELVAR</span><span>SOLVANE</span><span>BRUNT</span><span>TANQUELLE</span><span>VARUNO</span><span>UTO</span><span>TESKO</span>
  </div>
</section>
<div class="brand-arrow abs" style="left:0"><svg width="10" height="16" viewBox="0 0 10 16"><path d="M8 2 2 8l6 6" fill="none" stroke="#555" stroke-width="1.6"/></svg></div>
<div class="brand-arrow abs" style="left:1170px"><svg width="10" height="16" viewBox="0 0 10 16"><path d="m2 2 6 6-6 6" fill="none" stroke="#555" stroke-width="1.6"/></svg></div>

<h2 class="section-title abs" style="top:864px">About Us</h2>
<section class="about abs">
  <div class="about-photo abs" role="img" aria-label="Hand passing car keys to another hand beside a white car"></div>
  <div class="about-text abs">
    <p>We are a locally owned company with over 6 years of experience in the automotive industry. We provide towing and automotive locksmith services to the Dallas Ft-Worth Area.</p>
    <p>Our main goal is to provide unmatched customer service both to the client and your customer. You will appreciate the value of our professional approach to all your automotive needs. Our experienced staff will always be eager to assist you. We look forward to being your reliable business partner when your locksmith needs arise.</p>
    <p>Our business relationships with clients are warm, friendly and sincere. Our valued clients count on us to deliver excellent service and we're obliged to deliver above and beyond! We want every interaction you have with Cedarline Autoworks LLC to be refreshing and delightful; especially given the circumstances that brought you to us! We eliminate stress or incident.</p>
  </div>
</section>

<h2 class="section-title abs" style="top:1202px">Our Services</h2>
<section class="service-card recovery abs">
  <div class="tab abs" style="left:-6px;top:15px;width:211px;background:var(--teal)">Recovery Services</div>
  <ul class="service-list">
    <li><svg width="16" height="16" viewBox="0 0 16 16"><circle cx="8" cy="8" r="8" fill="var(--teal)"/><path d="m4.5 8 2.5 2.5 4.5-5" fill="none" stroke="#fff" stroke-width="1.8"/></svg>Involuntary Repossessions</li>
    <li><svg width="16" height="16" viewBox="0 0 16 16"><circle cx="8" cy="8" r="8" fill="var(--teal)"/><path d="m4.5 8 2.5 2.5 4.5-5" fill="none" stroke="#fff" stroke-width="1.8"/></svg>Voluntary Repossessions</li>
    <li><svg width="16" height="16" viewBox="0 0 16 16"><circle cx="8" cy="8" r="8" fill="var(--teal)"/><path d="m4.5 8 2.5 2.5 4.5-5" fill="none" stroke="#fff" stroke-width="1.8"/></svg>Skip Tracing</li>
    <li><svg width="16" height="16" viewBox="0 0 16 16"><circle cx="8" cy="8" r="8" fill="var(--teal)"/><path d="m4.5 8 2.5 2.5 4.5-5" fill="none" stroke="#fff" stroke-width="1.8"/></svg>Transportation of Vehicles (free delivery to any auction</li>
    <li><svg width="16" height="16" viewBox="0 0 16 16"><circle cx="8" cy="8" r="8" fill="var(--teal)"/><path d="m4.5 8 2.5 2.5 4.5-5" fill="none" stroke="#fff" stroke-width="1.8"/></svg>within the Metroplex)</li>
    <li><svg width="16" height="16" viewBox="0 0 16 16"><circle cx="8" cy="8" r="8" fill="var(--teal)"/><path d="m4.5 8 2.5 2.5 4.5-5" fill="none" stroke="#fff" stroke-width="1.8"/></svg>Secure Outdoor Storage</li>
  </ul>
</section>
<section class="service-card locksmith abs">
  <div class="tab abs" style="left:-6px;top:15px;width:314px;background:var(--navy)">Automotive locksmith Services</div>
  <ul class="service-list">
    <li><svg width="16" height="16" viewBox="0 0 16 16"><circle cx="8" cy="8" r="8" fill="var(--navy)"/><path d="m4.5 8 2.5 2.5 4.5-5" fill="none" stroke="#fff" stroke-width="1.8"/></svg>Lost cars keys and stolen car keys replaced</li>
    <li><svg width="16" height="16" viewBox="0 0 16 16"><circle cx="8" cy="8" r="8" fill="var(--navy)"/><path d="m4.5 8 2.5 2.5 4.5-5" fill="none" stroke="#fff" stroke-width="1.8"/></svg>Broken car keys</li>
    <li><svg width="16" height="16" viewBox="0 0 16 16"><circle cx="8" cy="8" r="8" fill="var(--navy)"/><path d="m4.5 8 2.5 2.5 4.5-5" fill="none" stroke="#fff" stroke-width="1.8"/></svg>Chip key programming/ Transponder keys</li>
    <li><svg width="16" height="16" viewBox="0 0 16 16"><circle cx="8" cy="8" r="8" fill="var(--navy)"/><path d="m4.5 8 2.5 2.5 4.5-5" fill="none" stroke="#fff" stroke-width="1.8"/></svg>Repair and rekey vehicle locks</li>
    <li><svg width="16" height="16" viewBox="0 0 16 16"><circle cx="8" cy="8" r="8" fill="var(--navy)"/><path d="m4.5 8 2.5 2.5 4.5-5" fill="none" stroke="#fff" stroke-width="1.8"/></svg>Car Lockouts</li>
  </ul>
</section>

<section class="coverage abs">
  <div class="coverage-photo abs" role="img" aria-label="Dallas downtown skyline under a blue sky"></div>
  <div class="tab abs" style="left:-6px;top:14px;width:211px;background:var(--navy)">Services Coverage</div>
  <p class="coverage-text abs">Our coverage includes the <b style="font-weight:600">DFW metroplex.</b><br>Call us for estimates outside the DFW area.</p>
</section>
<div class="coverage-phone abs">
  <span class="circle-icon" style="background:var(--teal)"><svg width="26" height="26" viewBox="0 0 24 24" fill="none" stroke="#fff" stroke-width="1.8"><path d="M6 3h4l2 5-2.5 1.5a11 11 0 0 0 5 5L16 12l5 2v4a2 2 0 0 1-2 2A16 16 0 0 1 4 5a2 2 0 0 1 2-2z"/></svg></span>
  888-555-0142
</div>

<section class="facility abs">
  <div class="tab abs" style="left:-6px;top:15px;width:209px;background:var(--red)">Our Facility</div>
  <span class="circle-icon abs" style="left:30px;top:127px;background:var(--red)"><svg width="22" height="26" viewBox="0 0 22 26" fill="none" stroke="#fff" stroke-width="1.8"><path d="M11 24s8-8.5 8-14a8 8 0 0 0-16 0c0 5.5 8 14 8 14z"/><circle cx="11" cy="10" r="3"/></svg></span>
  <p class="facility-text abs">Our facility is conveniently located<br>near Loop 9 and Harlow Blvd in Dallas Tx.<br>Our business hours are from<span class="facility-hours">10 am to 7pm.</span></p>
  <div class="facility-map abs" role="img" aria-label="Street map showing the facility location on Harlow Blvd"></div>
</section>

<h2 class="section-title abs" style="top:2107px;border-bottom:none">Customer Testimonials</h2>
<div class="testimonial-arrow abs" style="left:64px"><svg width="10" height="16" viewBox="0 0 10 16"><path d="M8 2 2 8l6 6" fill="none" stroke="#555" stroke-width="1.6"/></svg></div>
<div class="testimonial-arrow abs" style="left:1114px"><svg width="10" height="16" viewBox="0 0 10 16"><path d="m2 2 6 6-6 6" fill="none" stroke="#555" stroke-width="1.6"/></svg></div>
<div class="client-photo abs" role="img" aria-label="Portrait of the reviewing customer"></div>
<p class="quote abs">Professional and fast service. Cedarline Autoworks have work with<br>our company for less than a year . They are a fast towing company and their locksmith<br>services are one of the best in the DFW.<br><b>Brennan Auto Sales.</b></p>

<footer class="site-footer abs"></footer>
<div class="footer-card abs">
  <div class="brand-name">Cedarline Autoworks</div>
  <div class="footer-map abs" role="img" aria-label="Small street map of the Harlow Blvd location"></div>
</div>
<div class="footer-info abs">
  <h3>Cedarline Autoworks LLC.</h3>
  4120 Harlow BLVD<br>Dallas, TX 75211<br>
  <span style="display:block;margin-top:8px">Telephone: 888-555-0142</span>
  FAX: 2145550188<br>
  E-mail: <span class="mail">contact@cedarlineautoworks.example</span>
</div>
<div class="social abs"><span></span><span></span><span></span><span></span></div>
<svg class="footer-arrow abs" width="14" height="10" viewBox="0 0 14 10"><path d="M0 5h12M8 1l4 4-4 4" fill="none" stroke="var(--teal)" stroke-width="1.6"/></svg>
<ul class="footer-nav abs">
  <li>Home</li><li>About Us</li><li>Services</li><li>Locksmith Services</li><li>Price List</li><li>Contact Us</li><li>Privacy Policy</li>
</ul>
<div class="apps-title abs">Download Apps</div>
<div class="app-badge abs" style="top:2434px"></div>
<div class="app-badge abs" style="top:2490px"></div>
<div class="copyright abs">CEDARLINE AUTOWORKS LLC © 2014</div>

</body>
</html>
```